Software Development Consulting Company Needs Business Card Design

We need a new business card design for our consultants at Verdant Systems (verdantsystems.example). We are a small firm that provides high-end software development and methodology consulting to medium to large enterprise IT organizations.

Our logo uses Futura for the font and we would like to stick with navy blue and canary yellow for the logo colors. Attached are normal and reversed versions of our logos in illustrator format.
Updates

Hi Everyone, Thank yo very much for your amazing design ideas. I have created a poll for this project and our employees will be voting on the design they wish to use. We will be making a decision this Wednesday (October 22nd). Thanks again, Marcus Hallward

Industry/Entity Type

Business

```html
<!DOCTYPE html>
<html lang="en">
<head>
<meta charset="utf-8">
<title>Verdant Systems – Business Card Front and Back</title>
<link href="https://fonts.googleapis.com/css2?family=Oswald:wght@400;500;700&display=swap" rel="stylesheet">
<style>
  :root {
    --page-bg: #d9dadc;
    --card-white: #eeeff0;
    --navy: #1f3a66;
    --navy-light: #2d4f85;
    --canary: #f4d32c;
    --charcoal: #2c2d30;
    --paper-text: #ffffff;
  }
  * { margin: 0; padding: 0; box-sizing: border-box; }
  html, body {
    width: 1200px;
    height: 900px;
    overflow: hidden;
    background: var(--page-bg);
    font-family: "Oswald", "Arial Narrow", sans-serif;
  }
  .sheet {
    width: 1200px;
    height: 900px;
    display: flex;
    flex-direction: column;
    align-items: center;
    justify-content: center;
    gap: 44px;
  }
  .card {
    position: relative;
    width: 660px;
    height: 378px;
    overflow: hidden;
    box-shadow: 0 10px 24px rgba(0,0,0,0.22);
  }
  .card-art {
    position: absolute;
    inset: 0;
    width: 100%;
    height: 100%;
  }

  /* Front */
  .brand {
    position: absolute;
    left: 62px;
    top: 152px;
  }
  .brand-row {
    display: flex;
    align-items: center;
    gap: 14px;
  }
  .brand-mark {
    width: 28px;
    height: 28px;
    background: var(--canary);
  }
  .brand-name {
    font-weight: 700;
    font-size: 40px;
    line-height: 1;
    letter-spacing: 1px;
    color: var(--navy);
    white-space: nowrap;
  }
  .brand-tagline {
    margin-top: 9px;
    margin-left: 42px;
    font-weight: 500;
    font-size: 10.5px;
    letter-spacing: 1.4px;
    color: var(--charcoal);
    white-space: nowrap;
  }

  /* Back */
  .contact {
    position: absolute;
    left: 250px;
    top: 46px;
    color: var(--paper-text);
    text-transform: uppercase;
  }
  .person-name {
    font-weight: 500;
    font-size: 27px;
    letter-spacing: 1px;
    line-height: 1.1;
    white-space: nowrap;
  }
  .person-role {
    font-weight: 400;
    font-size: 12px;
    letter-spacing: 2px;
    margin-top: 4px;
    padding-left: 120px;
    color: var(--canary);
  }
  .contact-lines {
    list-style: none;
    margin-top: 22px;
    font-size: 13.5px;
    letter-spacing: 1.2px;
    line-height: 1.25;
  }
  .contact-lines li { margin-bottom: 14px; white-space: nowrap; }
  .icon-column {
    position: absolute;
    right: 40px;
    top: 110px;
    display: flex;
    flex-direction: column;
    gap: 14px;
  }
  .icon-tile {
    width: 32px;
    height: 32px;
    border-radius: 7px;
    background: var(--charcoal);
    display: flex;
    align-items: center;
    justify-content: center;
  }
  .icon-tile svg { width: 18px; height: 18px; }
</style>
</head>
<body>
<main class="sheet">

  <section class="card card-front" aria-label="Card front">
    <svg class="card-art" viewBox="0 0 660 378" aria-hidden="true">
      <defs>
        <linearGradient id="front-paper" x1="0" y1="0" x2="1" y2="1">
          <stop offset="0" stop-color="#f4f5f6"/>
          <stop offset="1" stop-color="#dedfe1"/>
        </linearGradient>
      </defs>
      <rect width="660" height="378" fill="url(#front-paper)"/>
      <polygon points="500,0 660,0 660,378 640,378" fill="#1f3a66"/>
      <polygon points="440,0 500,0 640,378 580,378" fill="#2c2d30"/>
    </svg>
    <div class="brand">
      <div class="brand-row">
        <span class="brand-mark"></span>
        <span class="brand-name">VERDANT SYSTEMS</span>
      </div>
      <p class="brand-tagline">QUALITY SOFTWARE CONSULTING DELIVERED</p>
    </div>
  </section>

  <section class="card card-back" aria-label="Card back">
    <svg class="card-art" viewBox="0 0 660 378" aria-hidden="true">
      <defs>
        <linearGradient id="back-navy" x1="0" y1="0" x2="1" y2="1">
          <stop offset="0" stop-color="#2d4f85"/>
          <stop offset="1" stop-color="#1c355e"/>
        </linearGradient>
      </defs>
      <rect width="660" height="378" fill="url(#back-navy)"/>
      <polygon points="0,150 0,378 228,378" fill="#eeeff0"/>
      <polygon points="0,70 0,150 228,378 308,378" fill="#2c2d30"/>
    </svg>

    <div class="contact">
      <h1 class="person-name">Tobias Renfield</h1>
      <p class="person-role">Director / CEO</p>
      <ul class="contact-lines">
        <li>+00 21 5550 - 0148</li>
        <li>renfield@verdantsystems.example</li>
        <li>www.verdantsystems.example</li>
        <li>580 Harbor Lane, North Bay<br>Porto Verde</li>
      </ul>
    </div>

    <div class="icon-column">
      <span class="icon-tile" aria-label="Phone">
        <svg viewBox="0 0 24 24"><path d="M6.6 10.8a15 15 0 0 0 6.6 6.6l2.2-2.2c.3-.3.7-.4 1-.2 1.1.4 2.3.6 3.6.6.6 0 1 .4 1 1V20c0 .6-.4 1-1 1A17 17 0 0 1 3 4c0-.6.4-1 1-1h3.5c.6 0 1 .4 1 1 0 1.3.2 2.5.6 3.6.1.3 0 .7-.2 1z" fill="#fff"/></svg>
      </span>
      <span class="icon-tile" aria-label="Email">
        <svg viewBox="0 0 24 24"><rect x="3" y="6" width="18" height="12" rx="1.5" fill="none" stroke="#fff" stroke-width="2"/><path d="M3.5 7l8.5 6 8.5-6" fill="none" stroke="#fff" stroke-width="2"/></svg>
      </span>
      <span class="icon-tile" aria-label="Website">
        <svg viewBox="0 0 24 24"><circle cx="12" cy="12" r="8.5" fill="none" stroke="#fff" stroke-width="1.8"/><path d="M3.5 12h17M12 3.5c3 3 3 14 0 17M12 3.5c-3 3-3 14 0 17" fill="none" stroke="#fff" stroke-width="1.5"/></svg>
      </span>
      <span class="icon-tile" aria-label="Address">
        <svg viewBox="0 0 24 24"><path d="M12 2.5a6.5 6.5 0 0 0-6.5 6.5c0 4.9 6.5 12.5 6.5 12.5s6.5-7.6 6.5-12.5A6.5 6.5 0 0 0 12 2.5z" fill="#fff"/><circle cx="12" cy="9" r="2.4" fill="#2c2d30"/></svg>
      </span>
    </div>
  </section>

</main>
</body>
</html>
```